Business Cards Needed for Innovative Healthcare Marketing Company

We are a marketing company focused on healthcare. Our company is all about rebranding yourself renewing your image and generating results. The phoenix stands for "reborn" or "rising" which we provide new brands for our clients we take their old brands and renew it with creativity and innovation. I am looking for a business card with color dimension. I have attached an example of a card I think has the look and feel of what I am trying to accomplish. I like that the card example has black and grey font colors, I like the font placement and the small logo, I really like the use of the colors on the right those are the colors of my logo. My logo is phoenix so maybe incorporating flames similar to that design. I would like the back a solid color maybe red with an opaque version of the logo and website. As a marketing company I am always open to creative liberty!

Target Market(s)

Doctors and business professionals.

Industry/Entity Type

Marketing

Contact Information for Business Card

Vornaly Health Care Marketing
Marnie Okonski- CEO
#(502)638-2947
email-marnie@vornaly.com
website- vornaly.com

Font styles to use
Sans Serif

Colors
ec1f27
f37122
ffc214
fbed22
fbf289
f04a50

Requirements
Must have
• The logo and required information
Nice to have
• icons by the information
Should not have
• child like font

```html
<!DOCTYPE html>
<html lang="en">
<head>
<meta charset="UTF-8">
<title>Vornaly Health Care Marketing – Business Card</title>
<link rel="stylesheet" href="https://fonts.googleapis.com/css2?family=Lato:wght@300;400;700&display=swap">
<style>
  :root {
    --brand-red: #ec1f27;
    --deep-red: #b81c24;
    --card-red: #d8252d;
    --brand-orange: #f37122;
    --brand-yellow: #ffc214;
    --soft-red: #f04a50;
    --ink: #3f3f3f;
    --ink-light: #5a5a5a;
    --paper: #ffffff;
    --backdrop: #ebe8e3;
  }
  * { margin: 0; padding: 0; box-sizing: border-box; }
  html, body {
    width: 780px; height: 1200px; overflow: hidden;
    background: var(--backdrop);
    font-family: "Lato", Arial, sans-serif;
  }
  .card {
    position: absolute; left: 70px;
    width: 640px; height: 366px;
    overflow: hidden;
    box-shadow: 0 10px 28px rgba(0,0,0,.18);
  }
  .card--front { top: 120px; background: var(--paper); }
  .card--back {
    top: 714px;
    background: linear-gradient(160deg, var(--brand-red) 0%, var(--card-red) 45%, var(--deep-red) 100%);
  }
  .card__art { position: absolute; inset: 0; width: 100%; height: 100%; }

  /* front */
  .brand { position: absolute; left: 46px; top: 88px; display: flex; align-items: center; gap: 12px; }
  .brand__dot { width: 34px; height: 34px; border-radius: 50%; background: var(--brand-orange); }
  .brand__name { font-size: 28px; font-weight: 400; color: var(--brand-red); letter-spacing: 1px; line-height: 1; }
  .brand__tagline { font-size: 8px; color: var(--brand-red); letter-spacing: 1.6px; margin-top: 4px; }
  .person { position: absolute; left: 46px; top: 196px; }
  .person__name { font-size: 27px; font-weight: 300; color: var(--ink); }
  .person__title { font-size: 15px; color: var(--brand-red); margin-top: 2px; }
  .contacts { position: absolute; left: 46px; top: 268px; list-style: none; }
  .contacts__item { display: flex; align-items: center; gap: 10px; font-size: 13.5px; color: var(--ink-light); height: 24px; }
  .contacts__icon { width: 14px; height: 14px; fill: var(--brand-red); }

  /* back */
  .back-brand { position: absolute; left: 0; right: 0; top: 116px; text-align: center; }
  .back-brand__name {
    display: inline-block; font-size: 72px; font-weight: 300; letter-spacing: 6px;
    color: rgba(255,255,255,.34); line-height: 1;
    padding: 0 10px 10px; border-bottom: 1px solid rgba(255,255,255,.3);
  }
  .back-brand__tagline { font-size: 17px; font-weight: 300; letter-spacing: 5px; color: rgba(255,255,255,.3); margin-top: 12px; }
</style>
</head>
<body>

<section class="card card--front" aria-label="Business card front">
  <svg class="card__art" viewBox="0 0 640 366" aria-hidden="true">
    <path d="M250 0 C390 18 480 130 520 366 L560 366 C520 135 432 24 300 0 Z" fill="var(--brand-yellow)" opacity=".75"/>
    <path d="M300 0 C432 24 520 135 560 366 L600 366 C562 140 474 28 360 0 Z" fill="var(--brand-orange)" opacity=".9"/>
    <path d="M360 0 C474 28 562 140 600 366 L640 366 L640 0 Z" fill="var(--card-red)"/>
    <path d="M330 0 C470 40 560 150 640 250 L640 0 Z" fill="var(--soft-red)" opacity=".35"/>
    <path d="M420 0 C520 60 590 160 640 330 L640 0 Z" fill="var(--brand-red)" opacity=".4"/>
  </svg>

  <div class="brand">
    <span class="brand__dot"></span>
    <div>
      <div class="brand__name">VORNALY</div>
      <div class="brand__tagline">HEALTH CARE MARKETING</div>
    </div>
  </div>

  <div class="person">
    <div class="person__name">Marnie Okonski</div>
    <div class="person__title">CEO</div>
  </div>

  <ul class="contacts">
    <li class="contacts__item">
      <svg class="contacts__icon" viewBox="0 0 16 16"><path d="M3 1h3l1.5 4-2 1.2a9 9 0 0 0 4.3 4.3L11 8.5l4 1.5v3a2 2 0 0 1-2 2A12 12 0 0 1 1 3a2 2 0 0 1 2-2z"/></svg>
      (502)638-2947
    </li>
    <li class="contacts__item">
      <svg class="contacts__icon" viewBox="0 0 16 16"><path d="M1 3h14v10H1z M1 3l7 6 7-6" fill="none" stroke="var(--brand-red)" stroke-width="1.6"/></svg>
      email-marnie@vornaly.com
    </li>
    <li class="contacts__item">
      <svg class="contacts__icon" viewBox="0 0 16 16"><g fill="none" stroke="var(--brand-red)" stroke-width="1.3"><circle cx="8" cy="8" r="6.5"/><ellipse cx="8" cy="8" rx="2.8" ry="6.5"/><path d="M1.5 8h13M2.5 4.8h11M2.5 11.2h11"/></g></svg>
      website- vornaly.com
    </li>
  </ul>
</section>

<section class="card card--back" aria-label="Business card back">
  <svg class="card__art" viewBox="0 0 640 366" aria-hidden="true">
    <path d="M0 0 H640 V120 C460 170 220 150 0 90 Z" fill="#ffffff" opacity=".07"/>
  </svg>
  <div class="back-brand">
    <div class="back-brand__name">VORNALY</div>
    <div class="back-brand__tagline">HEALTHCARE MARKETING</div>
  </div>
</section>

</body>
</html>
```